Crest Automotive Reconditioning Business Card

We need a professional business card that features our logo, a picture of the employee, and a brief list of our services.
I've attached a logo, and will attach photos at a later date.
The four services that need to be listed are Bumper repair and repainting, road rash repair, clear coat scratch repair, and automotive touch-up.
Target Market(s)
30 - 40 year male general managers of automobile dealerships. They are used to seeing every vendor gimmick under the sun. This brochure needs to impress with its simplicity and honesty.
Industry/Entity Type
Automotive
Look and feel
Each slider illustrates characteristics of the customer's brand and the style your logo design should communicate.

```html
<!DOCTYPE html>
<html lang="en">
<head>
<meta charset="utf-8">
<title>Crest Automotive Reconditioning – Business Card</title>
<link rel="stylesheet" href="https://fonts.googleapis.com/css2?family=Ubuntu:wght@400;500;700&display=swap">
<style>
  :root {
    --backdrop: #2a2a2a;
    --paper: #ffffff;
    --orange: #e8512a;
    --salmon: #ef8a6e;
    --charcoal: #1e1e1e;
    --grey: #5a5a5a;
    --muted: #8a8a8a;
    --photo-dark: #2b2b2b;
    --photo-light: #8c8c8c;
  }
  * { box-sizing: border-box; margin: 0; padding: 0; }
  html, body { width: 1200px; height: 1000px; overflow: hidden; }
  body {
    background: var(--backdrop);
    font-family: "Ubuntu", sans-serif;
    display: flex;
    flex-direction: column;
    align-items: center;
    justify-content: center;
    gap: 60px;
  }
  .card {
    position: relative;
    width: 700px;
    height: 400px;
    background: var(--paper);
    overflow: hidden;
  }
  .card-shapes { position: absolute; inset: 0; width: 100%; height: 100%; }
  .wordmark {
    position: absolute;
    color: var(--charcoal);
    font-weight: 700;
    line-height: 1;
  }
  .wordmark-name { display: block; font-size: 62px; letter-spacing: 2px; }
  .wordmark-tag { display: block; font-size: 15px; letter-spacing: 1px; margin-top: 6px; text-transform: uppercase; }

  /* Front */
  .card-front .wordmark { left: 48px; top: 50px; }
  .service-list {
    position: absolute;
    left: 48px;
    top: 198px;
    list-style: none;
    color: var(--paper);
    font-size: 19px;
    line-height: 25px;
  }
  .service-list li { position: relative; padding-left: 20px; }
  .service-list li::before {
    content: "";
    position: absolute;
    left: 2px;
    top: 9px;
    width: 6px;
    height: 6px;
    border-top: 2px solid var(--charcoal);
    border-right: 2px solid var(--charcoal);
    transform: rotate(45deg);
  }
  .web-address {
    position: absolute;
    right: 40px;
    bottom: 28px;
    color: var(--paper);
    font-size: 20px;
  }

  /* Back */
  .contact { position: absolute; left: 44px; top: 40px; }
  .contact-name { font-size: 26px; font-weight: 700; color: var(--charcoal); }
  .contact-role { font-size: 17px; color: var(--muted); margin-top: 2px; }
  .contact-lines { margin-top: 26px; font-size: 17px; line-height: 22px; color: var(--grey); }
  .card-back .wordmark { right: 44px; top: 86px; text-align: right; }
  .card-back .wordmark-name { font-size: 54px; }
  .card-back .wordmark-tag { font-size: 13px; }
  .company-block {
    position: absolute;
    right: 44px;
    top: 262px;
    color: var(--paper);
    font-size: 18px;
    line-height: 23px;
  }
  .company-name { font-weight: 700; font-size: 19px; }
  .label { color: var(--orange); }
</style>
</head>
<body>

  <article class="card card-front">
    <svg class="card-shapes" viewBox="0 0 700 400" aria-hidden="true">
      <defs>
        <linearGradient id="bandFade" x1="0" y1="0" x2="1" y2="0.4">
          <stop offset="0.45" stop-color="var(--orange)"/>
          <stop offset="1" stop-color="var(--salmon)"/>
        </linearGradient>
      </defs>
      <polygon points="0,172 700,172 700,292 0,330" fill="url(#bandFade)"/>
      <polygon points="0,352 700,306 700,400 0,400" fill="var(--grey)"/>
    </svg>
    <div class="wordmark">
      <span class="wordmark-name">CREST</span>
      <span class="wordmark-tag">Automotive Reconditioning</span>
    </div>
    <ul class="service-list">
      <li>Bumper Repair and Repainting</li>
      <li>Road Rash Repair</li>
      <li>Clear Coat Scratch Repair</li>
      <li>Automotive Touch-up</li>
    </ul>
    <p class="web-address">crestautomotive.com</p>
  </article>

  <article class="card card-back">
    <svg class="card-shapes" viewBox="0 0 700 400">
      <defs>
        <linearGradient id="photoTone" x1="0" y1="0" x2="1" y2="1">
          <stop offset="0" stop-color="var(--photo-dark)"/>
          <stop offset="0.6" stop-color="var(--photo-light)"/>
          <stop offset="1" stop-color="var(--photo-dark)"/>
        </linearGradient>
      </defs>
      <polygon points="0,240 700,215 700,400 0,400" fill="url(#photoTone)" role="img" aria-label="Black and white photograph of a car front wheel"/>
      <polygon points="0,196 700,196 700,215 0,240" fill="var(--orange)"/>
    </svg>
    <div class="contact">
      <h1 class="contact-name">Daniel Harrow</h1>
      <p class="contact-role">Accountant</p>
      <p class="contact-lines">02 5550 1420<br>daniel@crestautomotive.com</p>
    </div>
    <div class="wordmark">
      <span class="wordmark-name">CREST</span>
      <span class="wordmark-tag">Automotive Reconditioning</span>
    </div>
    <div class="company-block">
      <p class="company-name">CREST AUTOMOTIVE</p>
      <p>Wattle Street Kingsford NSW 2032</p>
      <p>02 5550 1420 <span class="label">Tel</span></p>
      <p>02 5550 1428 <span class="label">Fax</span></p>
    </div>
  </article>

</body>
</html>
```